Large corporation needs landing page for its employees with emotional and psychological problems

Vision:
Hello, we are a startup and would like to build a landing page and website in the mental health sector for a large corporation. In this site employees with emotional and psychological problems should quickly receive professional psychological support. This support takes the form of internal referrals from employees who are looking for help to qualified therapists, so that help can be provided quickly.
Furthermore, the employees get access to a tool where they can find out about topics in the mind health area and can also get help via webinars and podcasts. The employee should thus be able to take the hurdle to seek help and support in good time.
Therapists for whom the focus is on the urgency of providing quick help and support will work here in cooperation with the respective corporations.
Keywords:
• Help/Support
• overcome inhibitions
• Competent help
• Uncomplicated help
• Permanent access
• protected space
• Recognizing and naming emotional problems and actively tackling them
• get help
• mindfulness
• everyday helper
• Informative
• Anonymous
• compassion
• tolerance
• respect
• Appreciation
• empathy
• mindfulness
• protected space
• To be needed
• Like a lighthouse signal
What we need:
Landingpage
We need a landing page aimed at getting employees to contact psychological help. The call to action is to get in contact via a contact form.
Landing page content
There are several text modules:
• A heading/greeting
• A body of text at the beginning that explains the purpose of the page
• A bulleted text area describing the pain points and the solutions to them
Video:
The heart of the content will be a video explaining the need and inviting them to get in touch.
contact form:
It should be kept simple: first name, last name and email address
Legally required content:
General terms and conditions, data protection and imprint. These are only given as links in the footer.
In parallel, the Corporate Design should be adapted/extended:
Logo:
The font in the logo should be revised. The wings in the background remain.
Please adapt the logo for different uses:
• on a black background
• with transparent background
• favorite icon (browser)
• In square format for social media
Colors:
• develop a color chart based on the colors of the logo.
• please determine 2-3 main colors and the matching variations. I.e. transparent variations or light colors.
Typography:
Determine a decorative font and/or typography for headings and a text font. There should be no more than 3 fonts.
Updates
Need extra days to review
Industry/Entity Type
to recruit therapists as employees
Should not have
- please not to playful design or typography - and max. 3 colors

```html
<!DOCTYPE html>
<html lang="en">
<head>
<meta charset="utf-8">
<title>stillwater — landing page presentation</title>
<link rel="stylesheet" href="https://fonts.googleapis.com/css2?family=Fira+Sans:wght@400;500;600;700&family=Inter:wght@400;500&display=swap">
<style>
:root{
  --teal:#0b4f5e;
  --teal-deep:#083f4b;
  --teal-card:#0a4654;
  --accent:#1b8e98;
  --orange:#f29a05;
  --ice:#dcedf1;
  --ice-soft:#eef6f8;
  --ink:#1f2a2e;
  --muted:#5b6a70;
  --pill:#9fd1d7;
  --white:#ffffff;
}
*{box-sizing:border-box;margin:0;padding:0}
html,body{width:1200px;height:1200px;overflow:hidden}
body{font-family:"Inter",sans-serif;color:var(--ink)}
.canvas{position:relative;width:1200px;height:1200px;overflow:hidden;background:linear-gradient(135deg,#0f5662 0%,#3f7468 28%,#98a175 55%,#e3cc8f 78%,#f6dfa6 100%)}
.stage{position:absolute;left:0;top:0;width:1932px;height:1932px;overflow:hidden;transform:scale(0.621118);transform-origin:0 0}
.abs{position:absolute}
h1,h2,h3,.head{font-family:"Fira Sans",sans-serif}
.btn{position:absolute;background:var(--orange);color:#fff;border-radius:4px;display:flex;align-items:center;justify-content:center;font-size:11px;font-family:"Inter",sans-serif}
.pill{position:absolute;background:var(--pill);color:#fff;font-size:9px;border-radius:8px;padding:2px 8px}
.photo{position:absolute;border-radius:8px}

/* back page */
.page-back{position:absolute;left:1010px;top:0;width:708px;height:1724px;background:var(--white);border-radius:0 0 40px 0;overflow:hidden;box-shadow:0 20px 50px rgba(0,0,0,.18)}
.mini-card{position:absolute;top:-60px;width:142px;height:139px;border-radius:0 0 6px 6px;background:linear-gradient(180deg,#5c7a62 0%,#3d4a48 60%,#1d2b2f 100%)}
.mini-card .name{position:absolute;left:9px;bottom:26px;color:#fff;font:600 11px "Fira Sans",sans-serif}
.mini-card .more{position:absolute;left:9px;bottom:11px;color:#fff;font-size:8px;text-decoration:underline}
.band{position:absolute;left:0;width:100%;background:var(--teal)}
.feature{position:absolute;top:280px;width:141px;height:164px;background:var(--teal-card);border-radius:4px;color:#fff;font:600 11px/16px "Fira Sans",sans-serif;padding:10px}
.slider{position:absolute;display:flex;align-items:center;gap:6px}
.slider .dot{width:20px;height:20px;border-radius:50%;display:flex;align-items:center;justify-content:center}
.slider .line{height:2px;background:rgba(255,255,255,.6);position:relative}
.slider .line::before{content:"";position:absolute;left:0;top:0;height:2px;width:45%;background:var(--orange)}
.res-thumb{position:absolute;left:360px;width:166px;height:106px;border-radius:4px}
.res-text{position:absolute;left:538px;width:140px}
.res-text .cat{font-size:8px;color:var(--accent)}
.res-text .title{font:600 12.5px/17.5px "Fira Sans",sans-serif;margin-top:6px}
.res-text .link{font-size:7.5px;text-decoration:underline;margin-top:6px}
.contact-item{position:absolute;top:1200px;width:110px;height:43px;color:#fff;font-size:8.5px;text-align:center;display:flex;flex-direction:column;align-items:center;justify-content:center;gap:8px}
.form-card{position:absolute;left:142px;top:1267px;width:425px;height:291px;background:var(--ice-soft);border-radius:8px}
.label{position:absolute;font-size:8px;color:var(--ink)}
.field{position:absolute;background:var(--ice);border-radius:3px;display:flex;align-items:center;padding-left:10px;gap:9px;font-size:9px}

/* front page */
.page-front{position:absolute;left:213px;top:148px;width:934px;height:1784px;background:var(--white);border-radius:40px 40px 0 0;overflow:hidden;box-shadow:0 20px 60px rgba(0,0,0,.25)}
.logo{position:absolute;left:42px;top:24px;font:500 20px "Fira Sans",sans-serif;color:var(--teal);display:flex;align-items:center;gap:6px}
.logo .mark{width:8px;height:8px;border-radius:50%;background:var(--accent)}
.nav a{position:absolute;top:30px;font-size:10.5px;color:var(--ink);text-decoration:none}
.topic{position:absolute;top:692px;width:194px;height:124px;padding:20px 14px 0 21px;color:rgba(255,255,255,.72)}
.topic h3{font-size:14px;font-weight:600;margin-bottom:16px}
.topic p{font-size:9.6px;line-height:12.5px;letter-spacing:-.1px}
.topic.active{background:var(--teal-deep);color:#fff}
.team-card{position:absolute;top:1502px;width:187px;height:217px;border-radius:6px}
.team-card .name{position:absolute;left:12px;bottom:34px;color:#fff;font:600 14px "Fira Sans",sans-serif}
.team-card .more{position:absolute;left:12px;bottom:14px;color:#fff;font-size:10px;text-decoration:underline}
</style>
</head>
<body>
<div class="canvas">
<div class="stage">

  <section class="page-back" aria-label="Resources and contact page">
    <div class="mini-card" style="left:46px" role="img" aria-label="Portrait photo of therapist"><span class="name">Mina Park</span><span class="more">read more ↗</span></div>
    <div class="mini-card" style="left:204px;background:linear-gradient(180deg,#4f7d47,#3d4d4c 60%,#1d2b2f)" role="img" aria-label="Portrait photo of therapist"><span class="name">Graham Whitley</span><span class="more">read more ↗</span></div>
    <div class="mini-card" style="left:362px;background:linear-gradient(180deg,#3f6a5e,#33444a 60%,#1d2b2f)" role="img" aria-label="Portrait photo of therapist"><span class="name">Nora Castell</span><span class="more">read more ↗</span></div>
    <div class="mini-card" style="left:520px;background:linear-gradient(180deg,#c9b78f,#6d6858 60%,#1d2b2f)" role="img" aria-label="Portrait photo of therapist"><span class="name">Owen Marsh</span><span class="more">read more ↗</span></div>

    <div class="band" style="top:117px;height:415px"></div>
    <div class="abs head" style="left:10px;top:255px;width:260px;color:#fff;font:600 20px/25px 'Fira Sans',sans-serif">It’s your battle, but you<br>don’t need to fight alone.</div>
    <div class="abs" style="left:20px;top:315px;width:230px;color:#fff;font-size:7.5px;line-height:9.5px">Lorem ipsum dolor sit amet, consectetur adipiscing elit. Donec magna lobortis, vitae pretium quam volutpat ipsum ut placerat tincidunt lorem ex, sit amet tincidunt</div>
    <h2 class="abs" style="left:300px;top:155px;color:#fff;font-size:20px;line-height:25px;font-weight:600">It’s your battle, but you don’t need<br>to fight alone.</h2>
    <p class="abs" style="left:300px;top:216px;width:370px;color:#fff;font-size:7.5px;line-height:9.6px">Lorem ipsum dolor sit amet, consectetur adipiscing elit. Donec cursus ligula non magna lobortis, vitae pretium quam pharetra. Morbi volutpat ipsum ut placerat tincidunt. Cras consectetur lorem ex, sit amet tincidunt purus rhoncus id.</p>
    <div class="feature" style="left:300px">Lorem ipsum dolor.</div>
    <div class="feature" style="left:456px">Lorem ipsum dolor sit amet, consectetur.</div>
    <div class="feature" style="left:612px">Lorem ipsum dolor sit consectetur.</div>
    <div class="slider" style="left:300px;top:476px">
      <span class="dot" style="background:#2f6d5a"><svg width="10" height="10" viewBox="0 0 10 10"><path d="M8 5H2M5 2L2 5l3 3" stroke="#8fae5a" stroke-width="1.3" fill="none"/></svg></span>
      <span class="line" style="width:82px"></span>
      <span class="dot" style="background:#8a8c2a"><svg width="10" height="10" viewBox="0 0 10 10"><path d="M2 5h6M5 2l3 3-3 3" stroke="#f4c24a" stroke-width="1.3" fill="none"/></svg></span>
    </div>

    <h2 class="abs" style="left:121px;top:615px;font-size:18px;font-weight:500">Our experts</h2>
    <div class="abs" style="right:32px;top:624px;font-size:7.5px">View All Resources <span style="color:var(--orange)">→</span></div>
    <div class="abs" style="left:0;top:642px;width:676px;height:1px;background:#c9d3d6"></div>
    <div class="photo" style="left:100px;top:660px;width:239px;height:236px;background:linear-gradient(160deg,#efe9e2,#cfc6b8 55%,#8f8f7c)" role="img" aria-label="Photo of a counselling session in a bright room"></div>
    <h3 class="abs" style="left:140px;top:921px;font-size:12.5px;font-weight:600">How to Course Correct without</h3>
    <p class="abs" style="left:20px;top:962px;width:320px;font-size:7.5px;line-height:9.5px;color:var(--muted)">Lorem ipsum dolor sit amet, consectetur adipiscing elit. Sed id felis pretium, dapibus nulla vel fringilla mauris ut vulputate dignissim.</p>

    <div class="res-thumb" style="top:660px;background:linear-gradient(135deg,#2b5a55,#3f4b45 50%,#7e8fa8)" role="img" aria-label="Photo of a laptop on a video call beside a mug"></div>
    <div class="res-text" style="top:669px"><div class="cat">Podcast</div><div class="title">What Is the Grey Rock Method and Is It Effective?</div><div class="link">Listen now <span style="color:var(--orange)">↗</span></div></div>
    <div class="res-thumb" style="top:780px;background:linear-gradient(135deg,#d8d4cc,#8e7a6a 50%,#b05a4a)" role="img" aria-label="Video still of friends sharing a meal"></div>
    <svg class="abs" style="left:433px;top:822px" width="22" height="22" viewBox="0 0 22 22"><circle cx="11" cy="11" r="11" fill="#fff"/><path d="M9 7l6 4-6 4z" fill="#1f2a2e"/></svg>
    <div class="res-text" style="top:790px"><div class="cat">Video</div><div class="title">Does Success Lead to Happiness?</div><div class="link">Watch more <span style="color:var(--orange)">↗</span></div></div>
    <div class="res-thumb" style="top:901px;background:linear-gradient(135deg,#9a8a78,#d8c9a8 50%,#c7a33a)" role="img" aria-label="Photo of a supportive group conversation"></div>
    <div class="res-text" style="top:910px"><div class="cat">Article</div><div class="title">Can Depression Affect Your Empathy Levels?</div><div class="link">read more <span style="color:var(--orange)">↗</span></div></div>

    <div class="band" style="top:1063px;height:295px"></div>
    <span class="pill" style="left:328px;top:1101px;font-size:6.5px;background:#6fa3ad">Get In Touch</span>
    <h2 class="abs" style="left:0;width:708px;text-align:center;top:1117px;color:#fff;font-size:17.5px;font-weight:600">Get in touch, we're here for you</h2>
    <p class="abs" style="left:169px;width:370px;top:1152px;color:#fff;font-size:7.5px;line-height:9.5px;text-align:center">Lorem ipsum dolor sit amet, consectetur adipiscing elit. Donec cursus ligula non magna lobortis, vitae pretium quam pharetra.</p>
    <div class="contact-item" style="left:190px"><svg width="10" height="12" viewBox="0 0 10 12"><path d="M5 0a4 4 0 0 1 4 4c0 3-4 8-4 8S1 7 1 4a4 4 0 0 1 4-4z" fill="#2aa6ad"/><circle cx="5" cy="4" r="1.5" fill="#0b4f5e"/></svg>1187 Alder Lane, MS</div>
    <div class="contact-item" style="left:299px"><svg width="11" height="11" viewBox="0 0 11 11"><path d="M2 0l2 2.5-1.2 1.3a7 7 0 0 0 4.4 4.4L8.5 7 11 9l-1.5 2C4.5 11 0 6.5 0 1.5z" fill="#2aa6ad"/></svg>555-014-2287</div>
    <div class="contact-item" style="left:408px;background:var(--teal-deep);border-radius:3px"><svg width="12" height="9" viewBox="0 0 12 9"><rect width="12" height="9" rx="1" fill="#2aa6ad"/><path d="M0 1l6 4 6-4" stroke="#0b4f5e" fill="none"/></svg>hello@stillwater.example</div>

    <div class="form-card">
      <span class="label" style="left:27px;top:27px">Your Name</span>
      <div class="field" style="left:27px;top:43px;width:173px;height:33px"><svg width="10" height="10" viewBox="0 0 10 10"><circle cx="5" cy="5" r="4.3" fill="none" stroke="#1b8e98"/><circle cx="5" cy="4" r="1.5" fill="#1b8e98"/></svg>Jamie Rowe</div>
      <span class="label" style="left:27px;top:94px">Email</span>
      <div class="field" style="left:27px;top:110px;width:173px;height:33px;border:1.5px solid var(--accent);background:#f4fbfc"><svg width="11" height="8" viewBox="0 0 12 9"><rect width="12" height="9" rx="1" fill="#1b8e98"/><path d="M0 1l6 4 6-4" stroke="#fff" fill="none"/></svg><svg width="8" height="11" viewBox="0 0 8 11"><path d="M1 0v9l2-2 2 4 1-.5-2-4h3z" fill="#fff" stroke="#1f2a2e" stroke-width=".8"/></svg></div>
      <span class="label" style="left:26px;top:162px">Phone</span>
      <div class="field" style="left:27px;top:178px;width:173px;height:33px"><svg width="8" height="12" viewBox="0 0 8 12"><rect x=".5" y=".5" width="7" height="11" rx="1.5" fill="none" stroke="#1b8e98"/></svg></div>
      <span class="label" style="left:225px;top:27px">Message</span>
      <div class="field" style="left:225px;top:43px;width:173px;height:143px"></div>
      <div class="btn" style="left:171px;top:246px;width:83px;height:20px;font-size:8px">Send Message</div>
    </div>

    <div class="band" style="top:1640px;height:84px"></div>
    <div class="abs" style="right:32px;top:1666px;color:#fff;font-size:7.5px">Data protection and imprint &nbsp;•&nbsp; Terms and conditions</div>
    <div class="abs" style="left:142px;top:1683px;width:534px;height:1px;background:rgba(255,255,255,.5)"></div>
    <div class="abs" style="right:32px;top:1690px;color:#fff;font-size:7.5px">Copyright © 2023 stillwater</div>
  </section>

  <main class="page-front">
    <div class="abs" style="left:642px;top:0;width:292px;height:345px;background:var(--ice)"></div>
    <div class="logo"><span>stillwater</span><span class="mark"></span></div>
    <nav class="nav">
      <a style="left:328px;color:var(--accent)">Home</a>
      <a style="left:381px">Articles</a>
      <a style="left:442px">Diagnostic</a>
      <a style="left:516px">About</a>
      <a style="left:569px">Contact</a>
    </nav>
    <div class="btn" style="left:792px;top:22px;width:100px;height:27px">Get In Touch</div>

    <h1 class="abs" style="left:87px;top:122px;font-size:30px;line-height:40px;font-weight:600">Don’t let your <span style="color:var(--accent)">struggle</span><br>become your identity,<br>We got your back</h1>
    <p class="abs" style="left:87px;top:268px;width:310px;font-size:10px;line-height:13px;letter-spacing:-.1px;color:var(--ink)">Lorem ipsum dolor sit amet, consectetur adipiscing elit. Donec cursus ligula non magna lobortis, vitae pretium quam pharetra.</p>
    <div class="btn" style="left:87px;top:315px;width:99px;height:26px">Get In Touch</div>
    <div class="abs" style="left:216px;top:318px;display:flex;align-items:center;gap:8px;font-size:10.5px"><span style="text-decoration:underline">Watch Video</span><svg width="20" height="20" viewBox="0 0 20 20"><circle cx="10" cy="10" r="9" fill="none" stroke="#1f2a2e" stroke-width="1.3"/><path d="M8 6l6 4-6 4z" fill="#1f2a2e"/></svg></div>

    <div class="abs" style="left:0;top:398px;width:934px;height:597px;background:var(--teal)"></div>
    <div class="photo" style="left:417px;top:81px;width:486px;height:392px;background:linear-gradient(120deg,#e9ecec 0%,#dfe3e2 35%,#c9bba8 60%,#b99a80 75%,#8b8f95 100%)" role="img" aria-label="Photo of a therapist listening to a client on a sofa"></div>

    <span class="pill" style="left:43px;top:536px">What We Do</span>
    <h2 class="abs" style="left:43px;top:554px;color:#fff;font-size:25px;line-height:32px;font-weight:600">It’s your battle, but you don’t need<br>to fight alone, we can help you</h2>
    <div class="btn" style="left:799px;top:561px;width:92px;height:27px">Learn More</div>
    <p class="abs" style="left:43px;top:635px;width:620px;color:#fff;font-size:10px;line-height:13px;letter-spacing:-.1px">Lorem ipsum dolor sit amet, consectetur adipiscing elit. Donec cursus ligula non magna lobortis, vitae pretium quam pharetra. Morbi volutpat ipsum ut placerat tincidunt. Cras consectetur lorem ex, sit amet tincidunt purus rhoncus id.</p>

    <div class="topic" style="left:22px"><h3>Anxiety</h3><p>Lorem ipsum dolor sit amet, consectetur adipiscing elit. Donec cursus ligula non magna lobortis, vitae pretium quam pharetra.</p></div>
    <div class="topic active" style="left:222px"><h3>Phobia</h3><p>Lorem ipsum dolor sit amet, consectetur adipiscing elit. Donec cursus ligula non magna lobortis, vitae pretium quam pharetra.</p></div>
    <div class="topic" style="left:411px"><h3>Addiction</h3><p>Lorem ipsum dolor sit amet, consectetur adipiscing elit. Donec cursus ligula non magna lobortis, vitae pretium quam pharetra.</p></div>
    <div class="topic" style="left:606px"><h3>Despression</h3><p>Lorem ipsum dolor sit amet, consectetur adipiscing elit. Donec cursus ligula non magna lobortis, vitae pretium quam pharetra.</p></div>
    <div class="topic" style="left:801px"><h3>Anger</h3><p>Lorem ipsum dolor sit amet, consectetur adipiscing elit. Donec cursus ligula non magna lobortis, vitae pretium quam pharetra.</p></div>

    <div class="slider" style="left:718px;top:845px">
      <span class="dot" style="background:#2f6d5a;width:22px;height:22px"><svg width="10" height="10" viewBox="0 0 10 10"><path d="M8 5H2M5 2L2 5l3 3" stroke="#8fae5a" stroke-width="1.3" fill="none"/></svg></span>
      <span class="line" style="width:108px"></span>
      <span class="dot" style="background:#8a8c2a;width:22px;height:22px"><svg width="10" height="10" viewBox="0 0 10 10"><path d="M2 5h6M5 2l3 3-3 3" stroke="#f4c24a" stroke-width="1.3" fill="none"/></svg></span>
    </div>

    <div class="photo" style="left:131px;top:918px;width:672px;height:398px;border-radius:10px;background:linear-gradient(110deg,#eeeeec 0%,#d9d6d2 30%,#6b3a4a 52%,#a4552e 75%,#e7e3e0 100%)" role="img" aria-label="Video still of a counsellor taking notes while talking with a client"></div>
    <svg class="abs" style="left:416px;top:1078px" width="80" height="80" viewBox="0 0 80 80"><circle cx="40" cy="40" r="40" fill="#fff"/><path d="M32 24l24 16-24 16z" fill="#1a1a1a"/></svg>

    <span class="pill" style="left:43px;top:1404px">Meet Our Team</span>
    <h2 class="abs" style="left:43px;top:1426px;font-size:23px;font-weight:500">More experts on our team</h2>
    <div class="abs" style="right:42px;top:1434px;font-size:10px">meet all of us <span style="color:var(--orange);margin-left:6px">→</span></div>
    <div class="abs" style="left:43px;top:1460px;width:849px;height:1px;background:#c9d3d6"></div>

    <div class="team-card" style="left:62px;background:linear-gradient(180deg,#e8e8e6 0%,#8a6a6a 55%,#2a2e34 100%)" role="img" aria-label="Portrait photo of therapist"><span class="name">Mina Park</span><span class="more">read more ↗</span></div>
    <div class="team-card" style="left:270px;background:linear-gradient(180deg,#4f7d47 0%,#6d7f8a 55%,#1f2a30 100%)" role="img" aria-label="Portrait photo of therapist"><span class="name">Graham Whitley</span><span class="more">read more ↗</span></div>
    <div class="team-card" style="left:478px;background:linear-gradient(180deg,#b87856 0%,#5d6a5c 55%,#1d2328 100%)" role="img" aria-label="Portrait photo of therapist"><span class="name">Nora Castell</span><span class="more">read more ↗</span></div>
    <div class="team-card" style="left:686px;background:linear-gradient(180deg,#d6d2c8 0%,#b9a46a 55%,#2b3034 100%)" role="img" aria-label="Portrait photo of therapist"><span class="name">Owen Marsh</span><span class="more">read more ↗</span></div>

    <div class="abs" style="left:0;top:1769px;width:934px;height:15px;background:var(--teal)"></div>
  </main>

</div>
</div>
</body>
</html>
```